Thornvale plumbing business cards

Want a functional designed for my business cards using my logo

Company Name- Thornvale Plumbing, Heating & Water Systems
Name- Martin Thornvale
Title- Vice President
Cell- 555-318-7742
Email- Thornvaleplumbing@mailbrook.example
Business address-
PO Box 57
Alderwick, KT 21990

Plumbing

```html
<!DOCTYPE html>
<html lang="en">
<head>
<meta charset="utf-8">
<title>Thornvale Plumbing – Business Card</title>
<link rel="stylesheet" href="https://fonts.googleapis.com/css2?family=Open+Sans:wght@300;400;600;700&display=swap">
<style>
  :root {
    --page-bg: #e9e7e3;
    --blue-dark: #527aa8;
    --blue-light: #86a6cb;
    --white-panel: #f4f4f4;
    --accent-blue: #1f7fd1;
    --ink: #1d1f22;
    --phone-ink: #3f4652;
    --light-text: #ffffff;
  }
  html, body {
    margin: 0;
    padding: 0;
    width: 1200px;
    height: 1023px;
    overflow: hidden;
    background: var(--page-bg);
    font-family: "Open Sans", Arial, sans-serif;
  }
  .canvas {
    position: relative;
    width: 1200px;
    height: 1023px;
  }
  .card {
    position: absolute;
    left: 75px;
    top: 211px;
    width: 1050px;
    height: 600px;
    display: flex;
    box-shadow: 0 12px 30px rgba(0,0,0,0.25);
    overflow: hidden;
  }
  .brand-panel {
    position: relative;
    width: 590px;
    height: 100%;
    background: linear-gradient(160deg, var(--blue-light) 0%, var(--blue-dark) 75%);
  }
  .brand-name,
  .brand-tagline,
  .brand-phone {
    position: absolute;
    right: 30px;
    margin: 0;
    white-space: nowrap;
    text-align: right;
  }
  .brand-name {
    top: 275px;
    font-size: 50px;
    font-weight: 400;
    color: var(--light-text);
    letter-spacing: -0.5px;
  }
  .brand-tagline {
    top: 352px;
    font-size: 33px;
    font-weight: 300;
    color: var(--light-text);
  }
  .brand-phone {
    top: 430px;
    font-size: 52px;
    font-weight: 300;
    color: var(--phone-ink);
    letter-spacing: 1px;
  }
  .contact-panel {
    position: relative;
    flex: 1;
    height: 100%;
    background: var(--white-panel);
  }
  .person-name {
    position: absolute;
    left: 62px;
    top: 150px;
    margin: 0;
    font-size: 31px;
    font-weight: 700;
    color: var(--accent-blue);
  }
  .person-title {
    position: absolute;
    left: 62px;
    top: 196px;
    margin: 0;
    font-size: 22px;
    font-weight: 400;
    color: var(--ink);
  }
  .contact-list {
    position: absolute;
    left: 62px;
    top: 280px;
    margin: 0;
    padding: 0;
    list-style: none;
  }
  .contact-item {
    display: flex;
    align-items: flex-start;
    font-size: 18px;
    line-height: 30px;
    color: var(--ink);
    margin-bottom: 10px;
    white-space: nowrap;
  }
  .contact-icon {
    flex: none;
    width: 18px;
    height: 18px;
    margin: 6px 12px 0 0;
  }
</style>
</head>
<body>
<div class="canvas">
  <div class="card">
    <section class="brand-panel">
      <p class="brand-name">Thornvale Plumbing</p>
      <p class="brand-tagline">Heating &amp; Water Systems</p>
      <p class="brand-phone">555.204.6613</p>
    </section>
    <section class="contact-panel">
      <h1 class="person-name">Martin Thornvale</h1>
      <p class="person-title">Vice President</p>
      <ul class="contact-list">
        <li class="contact-item">
          <svg class="contact-icon" viewBox="0 0 18 18" aria-hidden="true">
            <rect width="18" height="18" rx="2" fill="var(--accent-blue)"/>
            <rect x="6" y="3" width="6" height="12" rx="1" fill="none" stroke="#fff" stroke-width="1.4"/>
          </svg>
          <span>555-318-7742</span>
        </li>
        <li class="contact-item">
          <svg class="contact-icon" viewBox="0 0 18 18" aria-hidden="true">
            <rect width="18" height="18" rx="2" fill="var(--accent-blue)"/>
            <rect x="3.5" y="5" width="11" height="8" fill="none" stroke="#fff" stroke-width="1.3"/>
            <path d="M3.5 5 L9 10 L14.5 5" fill="none" stroke="#fff" stroke-width="1.3"/>
          </svg>
          <span>Thornvaleplumbing@mailbrook.example</span>
        </li>
        <li class="contact-item">
          <svg class="contact-icon" viewBox="0 0 18 18" aria-hidden="true">
            <rect width="18" height="18" rx="2" fill="var(--accent-blue)"/>
            <path d="M9 15 C6 11 5 9 5 7.5 A4 4 0 0 1 13 7.5 C13 9 12 11 9 15 Z" fill="#fff"/>
            <circle cx="9" cy="7.5" r="1.5" fill="var(--accent-blue)"/>
          </svg>
          <span>PO Box 57<br>Alderwick, KT 21990</span>
        </li>
      </ul>
    </section>
  </div>
</div>
</body>
</html>
```